Referal Program Sign

Need two graphics layouts for banners to get printed one 20x20 and another 26x26 about our referral program. WE LOVE REFERRALS " Do you have friends and family that could use our services? Refer them to us and when they open a new agreement, you pick an agreement on your account for a two-week credit!

```html
<!DOCTYPE html>
<html lang="en">
<head>
<meta charset="utf-8">
<title>Norvale Furniture – Referral Program Banner</title>
<link rel="stylesheet" href="https://fonts.googleapis.com/css2?family=Montserrat:wght@500;600;700&family=Yellowtail&display=block">
<style>
  :root {
    --paper: #f4f1ec;
    --frame: #ffffff;
    --orange: #f2832f;
    --orange-shadow: #e3461c;
    --blue: #0e62a3;
    --green: #4fb64a;
    --ink: #231f20;
    --white: #ffffff;
  }
  * { margin: 0; padding: 0; box-sizing: border-box; }
  html, body {
    width: 1200px; height: 1200px; overflow: hidden;
    background: var(--frame);
  }
  .banner {
    position: relative; width: 1200px; height: 1200px;
    background: var(--frame); overflow: hidden;
    font-family: "Montserrat", Arial, sans-serif;
  }
  .banner-art { position: absolute; inset: 0; }

  .website {
    position: absolute; left: 78px; top: 194px;
    display: flex; align-items: center; gap: 10px;
    font-weight: 500; font-size: 36px; color: var(--ink);
    letter-spacing: 0.2px;
  }
  .website svg { width: 25px; height: 25px; }

  .brand {
    position: absolute; left: 565px; top: 90px;
    display: flex; align-items: center; gap: 26px;
  }
  .brand-ring {
    width: 232px; height: 232px; border-radius: 50%;
    border: 5px solid var(--orange); flex: none;
  }
  .brand-name {
    color: var(--blue); font-weight: 700; line-height: 1;
    width: 300px; white-space: nowrap;
  }
  .brand-name .line-1 { display: block; font-size: 58px; letter-spacing: 1px; }
  .brand-name .line-2 { display: block; font-size: 27px; letter-spacing: 9.5px; margin-top: 16px; }

  .script {
    font-family: "Yellowtail", "Brush Script MT", cursive;
    color: var(--white); white-space: nowrap;
    text-shadow: 2px 3px 0 var(--orange-shadow);
    font-weight: 400; line-height: 1;
  }
  .headline {
    position: absolute; left: 68px; top: 440px;
    font-weight: 400;
  }
  .headline-top { display: block; padding-left: 48px; height: 140px; }
  .headline-we { font-size: 80px; margin-right: 10px; }
  .headline-love { font-size: 140px; }
  .headline-referrals { display: block; font-size: 168px; }

  .question-lead {
    position: absolute; left: 112px; top: 784px;
    font-size: 38px; font-weight: 600; color: var(--white);
  }
  .question-script {
    position: absolute; left: 68px; top: 822px;
    font-size: 112px; text-shadow: none;
  }
  .question-tail {
    position: absolute; left: 114px; top: 912px;
    font-size: 40px; font-weight: 500; color: var(--white); letter-spacing: 0.5px;
  }
  .offer {
    position: absolute; left: 116px; top: 1014px;
    font-size: 25px; font-weight: 500; line-height: 35px;
    color: var(--white); letter-spacing: 0.6px; white-space: nowrap;
  }
</style>
</head>
<body>
<main class="banner">
  <svg class="banner-art" width="1200" height="1200" viewBox="0 0 1200 1200" aria-hidden="true">
    <defs>
      <clipPath id="panel-clip"><rect x="34" y="32" width="1134" height="1136"/></clipPath>
    </defs>
    <rect x="34" y="32" width="1134" height="1136" fill="var(--paper)"/>
    <g clip-path="url(#panel-clip)">
      <circle cx="230" cy="981" r="574" fill="var(--orange)"/>
      <circle cx="193" cy="869" r="494" fill="none" stroke="var(--orange)" stroke-width="1.3"/>
      <circle cx="298" cy="919" r="526" fill="none" stroke="var(--green)" stroke-width="1.3"/>
      <circle cx="298" cy="932" r="503" fill="none" stroke="var(--blue)" stroke-width="1.3"/>
    </g>
    <rect x="717" y="649" width="423" height="519" fill="var(--blue)" role="img" aria-label="Table lamp illustration in blue"/>
  </svg>

  <div class="website">
    <svg viewBox="0 0 24 24" aria-hidden="true">
      <circle cx="12" cy="12" r="10.5" fill="none" stroke="var(--green)" stroke-width="2"/>
      <ellipse cx="12" cy="12" rx="4.5" ry="10.5" fill="none" stroke="var(--green)" stroke-width="1.6"/>
      <line x1="1.5" y1="12" x2="22.5" y2="12" stroke="var(--green)" stroke-width="1.6"/>
      <line x1="3.5" y1="7" x2="20.5" y2="7" stroke="var(--green)" stroke-width="1.4"/>
      <line x1="3.5" y1="17" x2="20.5" y2="17" stroke="var(--green)" stroke-width="1.4"/>
    </svg>
    <span>norvalefurniture.us</span>
  </div>

  <div class="brand">
    <div class="brand-ring"></div>
    <div class="brand-name"><span class="line-1">NORVALE</span><span class="line-2">FURNITURE</span></div>
  </div>

  <h1 class="headline">
    <span class="headline-top"><span class="script headline-we">We</span><span class="script headline-love">Love</span></span>
    <span class="script headline-referrals">Referrals</span>
  </h1>

  <p class="question-lead">Do you have</p>
  <p class="script question-script">friends and family</p>
  <p class="question-tail">that could use our services?</p>

  <p class="offer">Refer them to us and when they open<br>a new agreement, you pick an agreement<br>on your account for a two-week credit!</p>
</main>
</body>
</html>
```